business card deign

Logo needs the following on it.
1. attached logo
2. Tagline - "If it keeps a drink cold or the party going...we do it!"
3. Name- Dalia Fenwick, Founder and CPO
4. Address - 482 E. Calder Avenue, Ste 2207, Tampa, FL. 33719
5. Phone - 720.555.0183

```html
<!DOCTYPE html>
<html lang="en">
<head>
<meta charset="UTF-8">
<title>Hopwell Business Card</title>
<link href="https://fonts.googleapis.com/css2?family=Montserrat:wght@400;600;700&display=swap" rel="stylesheet">
<style>
  :root {
    --backdrop: #9a9a9a;
    --card-light: #ffffff;
    --card-dark: #000000;
    --ink: #111111;
    --ink-soft: #2a2a2a;
    --paper-text: #f2f2f2;
    --rule: #1a1a1a;
  }
  * { margin: 0; padding: 0; box-sizing: border-box; }
  html, body {
    width: 1093px; height: 1200px; overflow: hidden;
    background: var(--backdrop);
    font-family: "Montserrat", Arial, sans-serif;
  }
  .stage { position: relative; width: 1093px; height: 1200px; }
  .card {
    position: absolute; left: 265px; width: 580px; height: 363px;
    border-radius: 18px; overflow: hidden;
  }
  .card--front { top: 225px; background: var(--card-light); color: var(--ink); }
  .card--back { top: 616px; background: var(--card-dark); color: var(--paper-text); }

  .brand-name {
    position: absolute; font-weight: 700; letter-spacing: 0.42em;
    white-space: nowrap; text-align: center;
  }
  .card--front .brand-name {
    left: 70px; width: 190px; top: 167px; font-size: 24px; color: var(--ink);
  }
  .card--back .brand-name {
    left: 0; width: 590px; top: 168px; font-size: 34px; color: var(--paper-text);
  }

  .divider {
    position: absolute; left: 281px; top: 108px; width: 1.5px; height: 180px;
    background: var(--rule);
  }
  .contact { position: absolute; left: 296px; top: 103px; }
  .contact__name { font-size: 21px; font-weight: 700; line-height: 1.2; color: var(--ink); }
  .contact__title { font-size: 12.5px; font-weight: 400; color: var(--ink-soft); margin-top: 1px; }
  .contact__address {
    font-size: 13px; line-height: 16px; color: var(--ink-soft); margin-top: 26px; padding-left: 1px;
  }
  .contact__list { list-style: none; margin-top: 19px; }
  .contact__item {
    display: flex; align-items: center; font-size: 13px; color: var(--ink-soft);
    height: 16px; margin-bottom: 11px;
  }
  .contact__icon { width: 12px; height: 12px; margin-right: 9px; flex: none; }

  .tagline {
    position: absolute; left: 0; width: 580px; top: 318px; text-align: center;
    font-size: 13px; font-weight: 400; color: var(--paper-text);
  }
</style>
</head>
<body>
<main class="stage">
  <section class="card card--front">
    <div class="brand-name">HOPWELL</div>
    <div class="divider"></div>
    <div class="contact">
      <div class="contact__name">Dalia Fenwick</div>
      <div class="contact__title">Founder and CPO</div>
      <div class="contact__address">482 E. Calder Avenue, Ste 2207,<br>Tampa, FL. 33719</div>
      <ul class="contact__list">
        <li class="contact__item">
          <svg class="contact__icon" viewBox="0 0 24 24" aria-hidden="true"><path fill="#111" d="M6.6 10.8a15.1 15.1 0 0 0 6.6 6.6l2.2-2.2c.3-.3.7-.4 1-.2 1.1.4 2.3.6 3.6.6.6 0 1 .4 1 1V20c0 .6-.4 1-1 1A17 17 0 0 1 3 4c0-.6.4-1 1-1h3.5c.6 0 1 .4 1 1 0 1.3.2 2.5.6 3.6.1.3 0 .7-.2 1z"/></svg>
          720.555.0183
        </li>
        <li class="contact__item">
          <svg class="contact__icon" viewBox="0 0 24 24" aria-hidden="true"><rect x="2" y="5" width="20" height="14" rx="2" fill="#111"/><path d="M3 6l9 7 9-7" stroke="#fff" stroke-width="1.6" fill="none"/></svg>
          info@hopwell.com
        </li>
        <li class="contact__item">
          <svg class="contact__icon" viewBox="0 0 24 24" aria-hidden="true"><circle cx="12" cy="12" r="10" fill="#111"/><path d="M12 2v20M2 12h20M5 6c4 2 10 2 14 0M5 18c4-2 10-2 14 0" stroke="#fff" stroke-width="1.4" fill="none"/></svg>
          www.hopwell.com
        </li>
      </ul>
    </div>
  </section>

  <section class="card card--back">
    <div class="brand-name">HOPWELL</div>
    <p class="tagline">If it keeps a drink cold or the party going...we do it</p>
  </section>
</main>
</body>
</html>
```